Harborline Crest Insurance Services

we are a high end insurance agency we specialize on Auto | Home | Business | Life looking for something professional and luxuries at the same time. if you guys need anything else please let me know.

Auto | Home | Business | Life must be under logo on the back with black background.

i want the back part to be black with our gold logo on it.

Target Market(s)

Auto | Home | Business | Life

Industry/Entity Type

Insurance Broker

Contact Information for Business Card

My logo is gold so a black in the back would be nice.

Font styles to use
Serif

Colors
000000

Requirements
Must have
• Big logo on the back with black background.

```html
<!DOCTYPE html>
<html lang="en">
<head>
<meta charset="utf-8">
<title>Harborline Crest Insurance Services — Business Cards</title>
<link rel="stylesheet" href="https://fonts.googleapis.com/css2?family=Cinzel:wght@600&family=Libre+Baskerville&family=Open+Sans:wght@400;700&display=swap">
<style>
  :root {
    --backdrop: #3a322d;
    --card-black: #141414;
    --card-edge: #0a0a0a;
    --gold: #e2b634;
    --silver: #c9c9c9;
    --white: #ffffff;
  }
  * { box-sizing: border-box; margin: 0; padding: 0; }
  html, body {
    width: 1200px;
    height: 818px;
    overflow: hidden;
    background: var(--backdrop);
  }
  .canvas {
    position: relative;
    width: 1200px;
    height: 818px;
  }
  .card {
    position: absolute;
    width: 540px;
    height: 309px;
    background: var(--card-black);
    border: 1px solid var(--card-edge);
    box-shadow: 0 14px 30px rgba(0, 0, 0, 0.45);
  }
  .card--back { left: 50px; top: 110px; }
  .card--front { left: 610px; top: 400px; }

  .brand-name {
    font-family: "Cinzel", serif;
    font-weight: 600;
    color: var(--gold);
    text-align: center;
    letter-spacing: 0.04em;
    line-height: 1.25;
  }
  .brand-mark {
    display: block;
    margin: 0 auto 14px;
    border-radius: 50%;
    background: var(--gold);
  }

  /* Back of card */
  .back-lockup {
    position: absolute;
    left: 0; right: 0; top: 62px;
  }
  .back-lockup .brand-mark { width: 46px; height: 46px; }
  .back-lockup .brand-name { font-size: 30px; }
  .back-lockup .brand-sub { font-size: 16px; letter-spacing: 0.3em; }
  .services {
    margin-top: 18px;
    font-family: "Open Sans", sans-serif;
    font-size: 15px;
    color: var(--silver);
    text-align: center;
    letter-spacing: 0.02em;
  }

  /* Front of card */
  .front-lockup {
    position: absolute;
    left: 26px; top: 88px;
    width: 230px;
  }
  .front-lockup .brand-mark { width: 34px; height: 34px; margin-bottom: 10px; }
  .front-lockup .brand-name { font-size: 17px; }
  .front-lockup .brand-sub { font-size: 10px; letter-spacing: 0.26em; }

  .contact {
    position: absolute;
    left: 300px; top: 104px;
    font-family: "Open Sans", sans-serif;
    color: var(--white);
  }
  .contact-name { font-size: 21px; line-height: 1.1; }
  .contact-name strong { font-weight: 700; }
  .contact-title {
    font-family: "Libre Baskerville", serif;
    font-size: 13px;
    color: var(--gold);
    margin: 2px 0 14px;
  }
  .contact-list { list-style: none; }
  .contact-list li {
    display: flex;
    align-items: center;
    gap: 9px;
    font-size: 14px;
    line-height: 25px;
  }
  .contact-list svg { width: 14px; height: 14px; flex: none; }
</style>
</head>
<body>
<main class="canvas">

  <section class="card card--back" aria-label="Back of business card">
    <div class="back-lockup">
      <span class="brand-mark"></span>
      <p class="brand-name">Harborline Crest<br><span class="brand-sub">Insurance Services</span></p>
      <p class="services">Auto | Home | Business | Life</p>
    </div>
  </section>

  <section class="card card--front" aria-label="Front of business card">
    <div class="front-lockup">
      <span class="brand-mark"></span>
      <p class="brand-name">Harborline Crest<br><span class="brand-sub">Insurance Services</span></p>
    </div>

    <div class="contact">
      <p class="contact-name">Your <strong>Name</strong></p>
      <p class="contact-title">Job Title</p>
      <ul class="contact-list">
        <li>
          <svg viewBox="0 0 16 16" aria-hidden="true"><path fill="#e2b634" d="M2 5c0-2 2-3 6-3s6 1 6 3v1h-3V5H5v1H2zM4 7h8l2 6H2z"/><circle cx="8" cy="10" r="1.6" fill="#141414"/></svg>
          000 000 0000
        </li>
        <li>
          <svg viewBox="0 0 16 16" aria-hidden="true"><rect x="1" y="3" width="14" height="10" fill="#e2b634"/><path d="M1 3l7 6 7-6" fill="none" stroke="#141414" stroke-width="1.3"/></svg>
          youremail@xyz.com
        </li>
        <li>
          <svg viewBox="0 0 16 16" aria-hidden="true"><g fill="none" stroke="#e2b634" stroke-width="1.3"><circle cx="8" cy="8" r="6.5"/><ellipse cx="8" cy="8" rx="2.8" ry="6.5"/><path d="M1.5 8h13M3 4.5h10M3 11.5h10"/></g></svg>
          yourwebsite.com
        </li>
      </ul>
    </div>
  </section>

</main>
</body>
</html>
```